Build a new Capability Statement for a labour support and maintenance company

Hi Everyone,
We wish to update our capability statement. Attached is a powerpoint that has the key ideas with random pictures we would like in the document. I have also attached a competitors document as a sample of the things we like. This document is being sent to our entire client base which includes Tier 1 mining companies like Vela Corran & KQS

Target Market(s)

Mining Companies

Industry/Entity Type

Mining

Colors

Designer to choose colors to be used in the design.

```html
<!DOCTYPE html>
<html lang="en">
<head>
<meta charset="utf-8">
<title>Redgum Plant &amp; Civil – Capability Statement</title>
<link href="https://fonts.googleapis.com/css2?family=Montserrat:wght@400;500;600;700&family=Oswald:wght@500;700&family=Yellowtail&display=swap" rel="stylesheet">
<style>
:root{
  --orange:#e8772e;
  --orange-deep:#b9652f;
  --ink:#1c1c1c;
  --text:#333;
  --grey-cell:#d9d9db;
  --page:#ffffff;
  --backdrop:#c4c4c7;
  --sky-top:#8a9a92;
  --sky-mid:#e3b890;
  --sky-low:#f2c9a0;
  --earth:#c4602a;
  --machine:#d9b52a;
}
*{margin:0;padding:0;box-sizing:border-box}
html,body{width:1200px;height:3434px;overflow:hidden}
body{background:var(--backdrop);font-family:'Montserrat',sans-serif;color:var(--text);position:relative}
.page{position:absolute;width:513px;height:727px;background:var(--page);overflow:hidden}
.cover{left:336px;top:127px}
.spread-1 .left{left:79px;top:929px}.spread-1 .right{left:592px;top:929px}
.spread-2 .left{left:79px;top:1740px}.spread-2 .right{left:592px;top:1740px}
.spread-3 .left{left:79px;top:2551px}.spread-3 .right{left:592px;top:2551px}

/* cover */
.cover-photo{position:absolute;inset:0;background:linear-gradient(180deg,var(--sky-top) 0%,var(--sky-mid) 30%,var(--sky-low) 52%,var(--earth) 72%,#6e5a2a 100%)}
.cover-photo::after{content:"";position:absolute;left:40px;right:0;bottom:0;height:330px;background:radial-gradient(ellipse at 45% 60%,var(--machine) 0%,rgba(217,181,42,.55) 35%,transparent 70%)}
.cover-banner{position:absolute;left:115px;top:0;width:282px;height:122px}
.cover-banner svg{position:absolute;left:0;top:0}
.cover-banner .brand{position:absolute;left:0;right:0;top:30px;text-align:center;color:#fff;font-weight:700;font-size:42px;letter-spacing:1px;line-height:1}
.cover-banner .sub{position:absolute;left:0;right:0;top:78px;text-align:center;color:#fff;font-size:9.5px;font-weight:500;letter-spacing:.5px}
.script-title{position:absolute;left:0;right:0;top:172px;text-align:center;font-family:'Yellowtail',cursive;color:var(--orange);font-size:66px;line-height:1}
.block-title{position:absolute;left:0;right:0;top:252px;text-align:center;font-family:'Oswald',sans-serif;font-weight:700;color:#111;font-size:98px;line-height:1;letter-spacing:-1px}

/* back cover */
.back{background:var(--orange-deep)}
.back-photo{position:absolute;inset:0;background:linear-gradient(160deg,#c26f37 0%,#a85a2b 45%,#8f4c25 70%,#b0632f 100%)}
.back-title{position:absolute;left:0;right:0;top:38px;text-align:center;font-family:'Oswald',sans-serif;font-weight:700;color:rgba(255,255,255,.32);font-size:64px;line-height:1.1}
.back-brand{position:absolute;left:0;right:0;top:510px;text-align:center;color:rgba(255,255,255,.45);font-weight:700;font-size:60px;line-height:1}
.back-brand-sub{position:absolute;left:0;right:0;top:578px;text-align:center;color:rgba(255,255,255,.5);font-size:13px;font-weight:500;letter-spacing:.5px}
.back-office{position:absolute;left:0;right:0;top:638px;text-align:center;color:#fff;font-weight:600;font-size:16px}
.back-address{position:absolute;left:0;right:0;top:660px;text-align:center;color:#fff;font-size:11px}
.back-email{position:absolute;left:190px;width:134px;top:677px;height:13px;border-radius:7px;background:#fff;color:var(--ink);font-size:7.5px;text-align:center;line-height:13px}

/* inner pages */
.tab{position:absolute;left:25px;top:0;width:112px;height:50px}
.tab svg{position:absolute;left:0;top:0}
.tab .brand{position:absolute;left:0;right:0;top:13px;text-align:center;color:#fff;font-weight:700;font-size:17px;line-height:1}
.tab .sub{position:absolute;left:0;right:0;top:31px;text-align:center;color:#fff;font-size:4.5px;letter-spacing:.3px}
.page-title{position:absolute;left:29px;font-weight:600;color:var(--ink);font-size:12px;line-height:1.2}
.page-title.big{color:var(--orange);font-size:24px;font-weight:600}
.tagline{position:absolute;left:29px;top:120px;font-size:9px;line-height:12px;color:var(--ink)}
.tagline span{border-bottom:1px solid var(--orange)}
.copy{position:absolute;left:29px;width:455px;font-size:8.4px;line-height:14px;color:var(--text);text-align:justify}
.copy p{margin-bottom:8px}
.copy b{color:var(--ink)}
.photo{position:absolute;background:linear-gradient(160deg,#7ea3c9 0%,#b9a882 45%,#d2ae3a 70%,#8b7b5d 100%)}
.photo.red{background:linear-gradient(170deg,#c9c3b9 0%,#b4b0a6 30%,#a34f2c 60%,#7a3a22 100%)}
.photo.shed{background:linear-gradient(170deg,#8b8a86 0%,#6f6a5f 45%,#c5a135 70%,#5d574c 100%)}
.footer-title{position:absolute;left:29px;top:664px;font-family:'Oswald',sans-serif;font-weight:500;font-size:21px;color:var(--ink);line-height:1}
.footer-band{position:absolute;left:0;right:0;top:690px;height:16px;background:var(--orange);color:#fff;display:flex;justify-content:space-between;align-items:center;padding:0 29px}
.footer-band .mail{font-size:11px}
.footer-band .folio{font-size:6.5px}
.list{position:absolute;left:29px;top:218px;font-size:8.4px;line-height:14px;color:var(--ink)}

/* projects table */
.projects{position:absolute;left:27px;top:107px;width:460px;display:grid;grid-template-columns:230px 105px 110px;column-gap:7px;row-gap:7px;font-size:7.2px;line-height:10.5px}
.projects .head{background:var(--orange);color:#fff;font-weight:500;font-size:10px;padding:6px 6px;height:26px}
.projects .cell{padding:5px 6px}
.projects .light{background:var(--grey-cell);color:var(--ink)}
.projects .dark{background:#0e0e0e;color:#fff}
</style>
</head>
<body>

<section class="page cover">
  <div class="cover-photo" role="img" aria-label="Yellow wheel loader in front of red earth under an evening sky"></div>
  <div class="cover-banner">
    <svg width="282" height="122" viewBox="0 0 282 122"><polygon points="0,0 282,0 282,100 141,122 0,100" fill="#e8772e"/></svg>
    <div class="brand">RPC</div>
    <div class="sub">REDGUM PLANT &amp; CIVIL</div>
  </div>
  <div class="script-title">Capability</div>
  <div class="block-title">STATEMENT</div>
</section>

<section class="spread-1">
  <div class="page left back">
    <div class="back-photo" role="img" aria-label="Orange toned photo of a loader in a mine yard"></div>
    <div class="back-title">REDGUM<br>PLANT &amp; CIVIL</div>
    <div class="back-brand">RPC</div>
    <div class="back-brand-sub">REDGUM PLANT &amp; CIVIL</div>
    <div class="back-office">HEAD OFFICE AND MAINTENANCE YARD</div>
    <div class="back-address">48 Ironbark Road Kelmore WA 6111</div>
    <div class="back-email">accounts@redgumpc.com.au</div>
  </div>
  <div class="page right">
    <div class="cover-photo" role="img" aria-label="Yellow wheel loader in front of red earth under an evening sky"></div>
    <div class="cover-banner">
      <svg width="282" height="122" viewBox="0 0 282 122"><polygon points="0,0 282,0 282,100 141,122 0,100" fill="#e8772e"/></svg>
      <div class="brand">RPC</div>
      <div class="sub">REDGUM PLANT &amp; CIVIL</div>
    </div>
    <div class="script-title">Capability</div>
    <div class="block-title">STATEMENT</div>
  </div>
</section>

<section class="spread-2">
  <div class="page left">
    <div class="tab"><svg width="112" height="50" viewBox="0 0 112 50"><polygon points="0,0 112,0 112,40 56,50 0,40" fill="#e8772e"/></svg><div class="brand">RPC</div><div class="sub">REDGUM PLANT &amp; CIVIL</div></div>
    <h1 class="page-title big" style="top:82px">Company Profile</h1>
    <p class="tagline">We believe our repeat clients are evidence<br><span>of our commitment to excellence</span></p>
    <div class="copy" style="top:160px">
      <p>Redgum Plant and Civil Pty Ltd (RPC) have a fully mobile workforce as well as an extensive schedule of plant and equipment to support any project.</p>
      <p>We are a family owned WA business backed by a loyal team of motivated and skilled individuals who are always available to meet your needs.</p>
      <p>We understand downtime can be costly to companies which is why RPC is committed to providing cost effective and efficient solutions for your business. Project objectives are always met with outstanding client service and field excellence.</p>
      <p>Since our inception in 2011 clients who engage RPC have become confident that they will receive professional, proficient and qualified people and plant on their jobs.</p>
      <p><b>Some past and present clients include Vela Corran, Ostrava Hire, Kestrel Ore, Meridian Build Pty Ltd, Tolland Industries, Brisk Mining, Fenwick Mining, Arlo Mining &amp; Arlo Civil</b></p>
    </div>
    <div class="photo" style="left:29px;top:373px;width:455px;height:238px" role="img" aria-label="Yellow wheel loader in a workshop yard under blue sky"></div>
    <div class="footer-title">CAPABILITY STATEMENT</div>
    <div class="footer-band"><span class="mail">accounts@redgumpc.com.au</span><span class="folio">Redgum Plant &amp; Civil / 2</span></div>
  </div>
  <div class="page right">
    <div class="tab"><svg width="112" height="50" viewBox="0 0 112 50"><polygon points="0,0 112,0 112,40 56,50 0,40" fill="#e8772e"/></svg><div class="brand">RPC</div><div class="sub">REDGUM PLANT &amp; CIVIL</div></div>
    <h1 class="page-title" style="top:80px">RPC Labour Support &amp; Rapid Response</h1>
    <div class="copy" style="top:124px">
      <p>RPC is available for rapid response, onsite support and maintenance 24/7 to keep your business and equipment powering. We offer full mechanical repairs, component rebuilds and exchanges, digger support and mining vehicle specification fit outs. RPC can source cost effective parts quality parts and OEM standards.</p>
      <p>Our dedicated team will ensure all projects are completed within specified timeframes ensuring the highest level of workmanship and safety is maintained</p>
    </div>
    <div class="photo red" style="left:28px;top:233px;width:455px;height:236px" role="img" aria-label="Dozers and a service ute on red earth at a mine site"></div>
    <div class="photo shed" style="left:31px;top:483px;width:129px;height:128px" role="img" aria-label="Service utes parked by a shed"></div>
    <div class="photo red" style="left:191px;top:483px;width:130px;height:128px" role="img" aria-label="Service ute beside machinery in an open pit"></div>
    <div class="photo red" style="left:353px;top:483px;width:130px;height:128px" role="img" aria-label="Excavator and service ute on a red dirt pad"></div>
    <div class="footer-title">CAPABILITY STATEMENT</div>
    <div class="footer-band"><span class="mail">accounts@redgumpc.com.au</span><span class="folio">Redgum Plant &amp; Civil / 3</span></div>
  </div>
</section>

<section class="spread-3">
  <div class="page left">
    <div class="tab"><svg width="112" height="50" viewBox="0 0 112 50"><polygon points="0,0 112,0 112,40 56,50 0,40" fill="#e8772e"/></svg><div class="brand">RPC</div><div class="sub">REDGUM PLANT &amp; CIVIL</div></div>
    <h1 class="page-title" style="top:78px">Ironbark Workshop</h1>
    <div class="copy" style="top:120px">
      <p>Located at 48 Ironbark Road Kelmore our workshop is equipped with skilled and knowledgeable staff, with all the required tooling, to perform your maintenance and servicing requirements as well as full machine rebuilds, fabrication works, component rebuilds, mine spec fit outs and much more.</p>
    </div>
    <h2 class="page-title" style="top:184px">Workshop facility</h2>
    <div class="list">11000 sqm yard capacity<br>Certified wash pad<br>Road train / float access</div>
    <div class="photo shed" style="left:29px;top:277px;width:99px;height:100px" role="img" aria-label="Grader on a trailer in the workshop"></div>
    <div class="photo shed" style="left:148px;top:277px;width:99px;height:100px" role="img" aria-label="Machines inside the workshop bays"></div>
    <div class="photo shed" style="left:267px;top:277px;width:99px;height:100px" role="img" aria-label="Bucket being repaired in the workshop"></div>
    <div class="photo shed" style="left:384px;top:277px;width:100px;height:100px" role="img" aria-label="Grader parked in the workshop"></div>
    <div class="photo shed" style="left:29px;top:395px;width:455px;height:105px" role="img" aria-label="White service truck inside the workshop"></div>
    <div class="photo shed" style="left:29px;top:513px;width:99px;height:100px" role="img" aria-label="Dozer in the workshop"></div>
    <div class="photo shed" style="left:148px;top:513px;width:99px;height:100px" role="img" aria-label="Machine under rebuild"></div>
    <div class="photo" style="left:267px;top:513px;width:99px;height:100px" role="img" aria-label="Wheel loader in the yard"></div>
    <div class="photo shed" style="left:384px;top:513px;width:100px;height:100px" role="img" aria-label="Dozer blade in the workshop"></div>
    <div class="footer-title">CAPABILITY STATEMENT</div>
    <div class="footer-band"><span class="mail">accounts@redgumpc.com.au</span><span class="folio">Redgum Plant &amp; Civil / 4</span></div>
  </div>
  <div class="page right">
    <div class="tab"><svg width="112" height="50" viewBox="0 0 112 50"><polygon points="0,0 112,0 112,40 56,50 0,40" fill="#e8772e"/></svg><div class="brand">RPC</div><div class="sub">REDGUM PLANT &amp; CIVIL</div></div>
    <h1 class="page-title" style="top:80px">Labour Support Projects</h1>
    <div class="projects">
      <div class="head">Project</div><div class="head">Machinery</div><div class="head">Client</div>
      <div class="cell light" style="height:43px">Ridge A – haul road and highway realignment overpass</div><div class="cell light">G14 Graders<br>G16 Grader<br>X33 Excavator</div><div class="cell light">Norvale</div>
      <div class="cell dark" style="height:52px">Corella Mine start up</div><div class="cell dark">T74 Dump Trucks<br>K9 Dozer<br>K8 Dozer<br>Service Truck</div><div class="cell dark">Quarry Civil</div>
      <div class="cell light" style="height:63px">Access road maintenance, drill pad / clearing</div><div class="cell light">G14 Graders<br>G15 Grader<br>Padfoot Roller<br>K10 Dozer<br>Tool Loader</div><div class="cell light">Delta Traffic /<br>Pindar Metals</div>
      <div class="cell dark" style="height:44px">Tallis 2 &amp; 4 - inter site access road build</div><div class="cell dark">G14 Grader<br>G16 Grader<br>X33 Excavator</div><div class="cell dark">Arlo Civil</div>
      <div class="cell light" style="height:63px">Copperline mine start up – building access track,<br>haul road and runway upgrade</div><div class="cell light">Watercart<br>K8 Dozer<br>G14 Grader<br>G16 Grader<br>X33 Excavator</div><div class="cell light">Arlo Civil &amp;<br>Arlo Mining</div>
      <div class="cell dark" style="height:23px">Saltbush Ridge</div><div class="cell dark">T74 Artic Dump Trucks</div><div class="cell dark">Corbel Plant Holdings</div>
      <div class="cell light" style="height:57px">Sable Gold -tailing dam upgrade and access road<br>maintenance</div><div class="cell light">50T Excavator<br>G14</div><div class="cell light">Heron Contracting</div>
      <div class="cell dark" style="height:46px">Wren Gap – runway upgrade</div><div class="cell dark">G14 Grader<br>G16 Grader</div><div class="cell dark">Norvale / KQS</div>
    </div>
    <div class="footer-title">CAPABILITY STATEMENT</div>
    <div class="footer-band"><span class="mail">accounts@redgumpc.com.au</span><span class="folio">Redgum Plant &amp; Civil / 5</span></div>
  </div>
</section>

</body>
</html>
```